New Business Cards for Torvin Group

We need a new Business Card to compliment our new logo. We are a vibrant design, manufacture and install business providing recreation areas, public parks and Municipal spaces. We want business cards that are classy, modern and clean.

We have recently changed our logo, and are celebrating our 40th anniversary. We want business cards with a new modern design to reflect our status.

Target Market(s)

Customers

Contact Information for Business Card

We need all the details of our 3 offices as per the business card attached. Please disregard the old logo on the business card, the other three files show our new logo.

Requirements
Must have
• All info as per attached business card but with new logo.
Nice to have

```html
<!DOCTYPE html>
<html lang="en">
<head>
<meta charset="utf-8">
<title>Torvin Group – Business Card</title>
<link href="https://fonts.googleapis.com/css2?family=Lato:wght@400;700&display=swap" rel="stylesheet">
<style>
  :root {
    --red: #e0383b;
    --red-light: #e84c4f;
    --black: #111111;
    --charcoal: #1e1e1e;
    --white: #ffffff;
    --ink: #222222;
    --stage: #e9e9e9;
  }
  * { box-sizing: border-box; margin: 0; padding: 0; }
  html, body { width: 1200px; height: 900px; overflow: hidden; }
  body {
    background: var(--stage);
    font-family: "Lato", sans-serif;
    position: relative;
  }
  .card {
    position: absolute;
    left: 250px;
    width: 700px;
    height: 400px;
    overflow: hidden;
    box-shadow: 0 6px 18px rgba(0,0,0,.18);
  }

  /* Back side */
  .card-back { top: 30px; background: linear-gradient(135deg, #0c0c0c, #1a1a1a 60%, #0d0d0d); }
  .card-back .world-map {
    position: absolute; inset: 30px 40px 60px;
    background: radial-gradient(ellipse at center, rgba(60,60,60,.45), rgba(30,30,30,0) 70%);
  }
  .card-back .brand {
    position: absolute; top: 140px; left: 0; right: 0;
    display: flex; align-items: center; justify-content: center; gap: 18px;
  }
  .brand-dot { width: 70px; height: 70px; border-radius: 50%; background: var(--red); }
  .card-back .brand-name { color: var(--white); font-size: 46px; font-weight: 700; letter-spacing: 2px; }
  .card-back .established {
    position: absolute; top: 268px; left: 0; right: 0; text-align: center;
    color: var(--white); font-size: 15px;
  }
  .card-back .website {
    position: absolute; bottom: 26px; left: 0; right: 0; text-align: center;
    color: var(--red); font-size: 15px; letter-spacing: 3px;
  }

  /* Front side */
  .card-front { top: 470px; background: var(--white); }
  .holder { position: absolute; top: 26px; left: 40px; }
  .holder-name { font-size: 30px; color: var(--ink); font-weight: 400; }
  .holder-role { font-size: 15px; color: var(--red); margin-top: 2px; }
  .holder-contacts { list-style: none; margin-top: 16px; }
  .holder-contacts li { display: flex; align-items: center; gap: 12px; font-size: 15px; color: var(--ink); margin-bottom: 8px; }
  .holder-contacts svg { width: 18px; height: 18px; }
  .card-front .brand {
    position: absolute; top: 62px; right: 40px;
    display: flex; align-items: center; gap: 12px;
  }
  .card-front .brand-dot { width: 54px; height: 54px; }
  .card-front .brand-name { color: var(--ink); font-size: 30px; font-weight: 700; letter-spacing: 1px; }

  .offices-band {
    position: absolute; top: 188px; left: 0; right: 0; height: 150px;
    background: var(--charcoal);
    border-top: 3px solid var(--red);
    display: flex; padding: 12px 40px 0;
  }
  .office { flex: 1; color: var(--white); font-size: 13.5px; line-height: 1.5; }
  .office-title { color: var(--red); font-size: 14.5px; margin-bottom: 3px; font-weight: 400; }
  .office .label { color: var(--red); }
  .web-band {
    position: absolute; top: 338px; left: 0; right: 0; bottom: 0;
    border-top: 4px solid var(--white);
    background: linear-gradient(90deg, var(--red), var(--red-light));
    color: var(--white); font-size: 16px; letter-spacing: 4px;
    display: flex; align-items: center; justify-content: center;
  }
</style>
</head>
<body>

<section class="card card-back" aria-label="Card back">
  <div class="world-map" role="img" aria-label="Faint world map in the background"></div>
  <div class="brand">
    <span class="brand-dot"></span>
    <span class="brand-name">TORVIN GROUP</span>
  </div>
  <p class="established">Est. 1979</p>
  <p class="website">www.torvingroup.com</p>
</section>

<section class="card card-front" aria-label="Card front">
  <div class="holder">
    <h1 class="holder-name">Rami Haddad</h1>
    <p class="holder-role">Managing Partner</p>
    <ul class="holder-contacts">
      <li>
        <svg viewBox="0 0 18 18" aria-hidden="true"><rect x="5" y="1.5" width="8" height="15" rx="1.5" fill="none" stroke="#e0383b" stroke-width="1.6"/><line x1="8" y1="14" x2="10" y2="14" stroke="#e0383b" stroke-width="1.4"/></svg>
        +971 (0)50 555 0142
      </li>
      <li>
        <svg viewBox="0 0 18 18" aria-hidden="true"><rect x="1.5" y="4" width="15" height="10" fill="#e0383b"/><polyline points="1.5,4 9,10 16.5,4" fill="none" stroke="#ffffff" stroke-width="1.2"/></svg>
        rami@torvingroup.com
      </li>
    </ul>
  </div>

  <div class="brand">
    <span class="brand-dot"></span>
    <span class="brand-name">TORVIN GROUP</span>
  </div>

  <div class="offices-band">
    <div class="office">
      <h2 class="office-title">Head Office</h2>
      <p>P.O. Box: 31480</p>
      <p>Abu Dhabi, U.A.E</p>
      <p><span class="label">T:</span> +971 (0)2 5550184</p>
      <p><span class="label">F:</span> +971 (0)2 5550185</p>
      <p><span class="label">E:</span> sales@torvingroup.com</p>
    </div>
    <div class="office">
      <h2 class="office-title">Dubai Office</h2>
      <p>P.O. Box: 402716</p>
      <p>Dubai, U.A.E</p>
      <p><span class="label">T:</span> +971 (0)4 5550391</p>
      <p><span class="label">F:</span> +971 (0)4 5550392</p>
      <p><span class="label">E:</span> sales@torvingroup.com</p>
    </div>
    <div class="office">
      <h2 class="office-title">Qatar Office</h2>
      <p>P.O. Box: 17203</p>
      <p>Doha, Qatar</p>
      <p><span class="label">T:</span> +974 55502871</p>
      <p><span class="label">F:</span> +974 55502871</p>
      <p><span class="label">E:</span> sales@torvingroup.com</p>
    </div>
  </div>

  <div class="web-band">www.torvingroup.com</div>
</section>

</body>
</html>
```